Ghost Tour and Pub Crawl Rack Card Brochure

We are looking to get an updated design for our rack cards that are printed on 4x9 vertical cards. We have uploaded our logo and our previous design. We are looking for a new idea. We need something that jumps out at you when they are printed and sitting next to a group of 50 other brochures. It needs to have all of the must haves incorporated.

Target Market(s)

Women

Industry/Entity Type

Tourism

Font styles to use
Serif
Sans Serif
Decorative
Script
Other font styles liked:
• Doesn't Matter

Colors

Designer to choose colors to be used in the design.

Requirements
Must have
• Needs to be a design that jumps out at you when you are looking at 50 of these in a rack from all different companies.
• 1. Instead of it being just Ghost Tour Pub Crawl, we would like it to have some sort of design that is Ghost Tours and Pub Crawls.
• 2. Our Website must be prominent www.DuskLanternWalks.com
• 2. We want a box for text at the bottom that we can add a promo code ourselves to the design, so just something that we can edit later that allows us to have enough space to write a promo code, city name, and alternate phone number.
• 3. We want it to say save 10% instead of $5.00
• 4. Phone number 1-8-Moon-Walk listed on the card
Nice to have
• Needs to be Spooky, but stand out.

```html
<!DOCTYPE html>
<html lang="en">
<head>
<meta charset="utf-8">
<title>Ghost Tour and Pub Crawl Rack Card</title>
<link href="https://fonts.googleapis.com/css2?family=Rye&family=Monoton&family=Kelly+Slab&family=Oswald:wght@500;700&family=Kaushan+Script&display=swap" rel="stylesheet">
<style>
  :root {
    --page-bg: #f2f2f2;
    --card-bg: #080506;
    --blood-red: #d8241c;
    --dark-maroon: #2a0a10;
    --shadow-purple: #3a1530;
    --neon-yellow: #ffe45a;
    --neon-glow: #ffb400;
    --ghost-white: #f4eef0;
    --promo-red: #e0261e;
  }
  * { margin: 0; padding: 0; box-sizing: border-box; }
  html, body {
    width: 1200px; height: 1000px; overflow: hidden;
    background: var(--page-bg);
  }
  .rack-card {
    position: absolute; left: 395px; top: 15px;
    width: 415px; height: 937px;
    background: var(--card-bg);
    overflow: hidden;
  }
  .hero-photo {
    position: absolute; left: 0; top: 190px; width: 100%; height: 640px;
    background:
      radial-gradient(ellipse 30% 26% at 50% 30%, #0a0405 0%, #0a0405 50%, rgba(10,4,5,0) 75%),
      radial-gradient(ellipse 60% 45% at 52% 28%, #a2181a 0%, #6a0e12 45%, transparent 75%),
      radial-gradient(ellipse 70% 40% at 40% 70%, #4a2630 0%, #25121a 50%, transparent 80%),
      linear-gradient(90deg, var(--dark-maroon) 0%, #1a0608 18%, #1a0608 82%, var(--shadow-purple) 100%);
  }
  .hero-photo::after {
    content: ""; position: absolute; inset: 0;
    background: linear-gradient(180deg, var(--card-bg) 0%, transparent 12%, transparent 65%, var(--card-bg) 100%);
  }
  .title { position: absolute; top: 38px; width: 100%; text-align: center; }
  .title-ghost {
    font-family: "Rye", serif; font-size: 44px; color: var(--blood-red);
    letter-spacing: 1px; line-height: 1;
  }
  .title-and {
    font-family: "Kaushan Script", cursive; font-size: 14px; color: var(--neon-yellow);
    text-shadow: 0 0 6px var(--neon-glow); line-height: 1;
  }
  .title-pub {
    font-family: "Monoton", sans-serif; font-size: 46px; color: var(--neon-yellow);
    text-shadow: 0 0 6px var(--neon-glow), 0 0 16px var(--neon-glow);
    line-height: 1.05; margin-left: 20px;
  }
  .offer {
    position: absolute; top: 440px; width: 100%;
    display: flex; justify-content: center; align-items: center; gap: 12px;
    font-family: "Oswald", sans-serif; font-weight: 700; color: var(--ghost-white);
  }
  .offer-save { font-size: 40px; line-height: 1; }
  .offer-amount { font-size: 68px; line-height: 1; }
  .offer-per { display: flex; flex-direction: column; align-items: center; line-height: 1; }
  .offer-per small { font-size: 15px; }
  .offer-per span { font-size: 32px; }
  .brand {
    position: absolute; top: 700px; width: 100%;
    font-family: "Kelly Slab", sans-serif; font-size: 32px; color: var(--ghost-white);
    display: flex; justify-content: center; align-items: center; gap: 8px;
  }
  .brand-dot { width: 10px; height: 10px; border-radius: 50%; background: var(--ghost-white); }
  .promo-label {
    position: absolute; top: 752px; width: 100%; text-align: center;
    font-family: "Oswald", sans-serif; font-weight: 700; font-size: 18px; line-height: 1.2;
    color: var(--promo-red); text-transform: uppercase;
  }
  .promo-box {
    position: absolute; top: 780px; left: 67px; width: 281px; height: 62px;
    border: 2px solid var(--promo-red);
  }
  .contact {
    position: absolute; top: 852px; width: 100%; text-align: center;
    font-family: "Oswald", sans-serif; font-weight: 700;
    color: var(--ghost-white); text-transform: uppercase;
  }
  .contact-web { font-size: 23px; line-height: 1.2; letter-spacing: 0.5px; }
  .contact-or { font-size: 13px; line-height: 1.3; }
  .contact-phone { font-size: 20px; line-height: 1.2; }
</style>
</head>
<body>
  <main class="rack-card">
    <div class="hero-photo" role="img" aria-label="Dark photo of a shadowy figure reaching toward the viewer against a red glowing doorway"></div>

    <header class="title">
      <div class="title-ghost">GHOST TOUR</div>
      <div class="title-and">and</div>
      <div class="title-pub">PUB CRAWL</div>
    </header>

    <section class="offer">
      <span class="offer-save">SAVE</span>
      <span class="offer-amount">10%</span>
      <span class="offer-per"><small>PER</small><span>TICKET</span></span>
    </section>

    <div class="brand"><span class="brand-dot"></span>Dusk Lantern Walks</div>

    <div class="promo-label">Use promo code:</div>
    <div class="promo-box"></div>

    <footer class="contact">
      <div class="contact-web">www.DuskLanternWalks.com</div>
      <div class="contact-or">or call</div>
      <div class="contact-phone">1-8-Moon-Walk</div>
    </footer>
  </main>
</body>
</html>
```